Create a new email template des

We are looking for 2 email template designed similar to the attached supplied like Inn Quickly in order to promote of photography business and also our marketing agency.

Both similar in design and branding but with a slight change to the body area.

1. Email is to show images and a little text as attached.
2. Email is to show more text and longer emails with tips and best practices education.

Our website is: www.corvanmeadow.com

The photography site is: http://corvanmeadow.com/hotel-photography/

Target Market(s)

Luxury Hotels

Industry/Entity Type

Business

Requirements
Must have
• Stylish design and as per breif

```html
<!DOCTYPE html>
<html lang="en">
<head>
<meta charset="utf-8">
<title>Corvan Meadow – Email Template 1</title>
<link rel="stylesheet" href="https://fonts.googleapis.com/css2?family=Jost:wght@400;500&family=Oswald:wght@300;400&display=swap">
<style>
  :root{
    --ink:#000;
    --text:#2b2b2b;
    --paper:#fff;
    --mist:#ebebeb;
    --stage:#fff;
    --shadow:rgba(0,0,0,.38);
    --font-body:"Jost", "Helvetica Neue", Arial, sans-serif;
    --font-head:"Oswald", "Arial Narrow", sans-serif;
  }
  *{box-sizing:border-box;margin:0;padding:0}
  html,body{width:1200px;height:1000px;overflow:hidden;background:var(--stage)}
  body{position:relative;font-family:var(--font-body);color:var(--text)}

  .board-title{position:absolute;left:42px;top:34px;font-family:var(--font-head);font-weight:400;font-size:22px;letter-spacing:2px;color:var(--ink)}

  .sheet{position:absolute;overflow:hidden;background:var(--paper)}
  .sheet--full{left:38px;top:85px;width:239px;height:875px}
  .sheet--full .email{transform:scale(.602);transform-origin:0 0}
  .sheet--upper{left:333px;top:83px;width:397px;height:730px;box-shadow:14px 20px 26px var(--shadow)}
  .sheet--lower{left:758px;top:121px;width:397px;height:717px;box-shadow:14px 20px 26px var(--shadow)}
  .sheet--lower .pair{height:194px}

  .email{width:397px;background:var(--paper)}

  .masthead{height:68px;background:var(--ink);display:flex;align-items:center;padding-left:24px}
  .brand{font-family:var(--font-body);font-weight:400;font-size:14px;letter-spacing:1.2px;color:var(--paper);text-transform:uppercase}

  .photo{display:block}
  .hero{position:relative;height:206px;
    background:
      radial-gradient(ellipse 60% 30% at 70% 62%,rgba(150,170,190,.35),transparent 70%),
      linear-gradient(180deg,#2e3460 0%,#4a5384 30%,#6a7699 52%,#4d6a78 64%,#2f7f8a 78%,#1f4e57 90%,#2a3236 100%)}
  .hero-title{position:absolute;left:22px;top:47px;font-family:var(--font-head);font-weight:300;font-size:29px;line-height:37px;color:var(--paper);text-transform:uppercase;letter-spacing:0}

  .copy{font-size:8px;line-height:15.2px;text-align:justify;color:var(--text)}
  .intro{height:115px;padding:23px 22px 0}
  .button{display:block;width:85px;height:22px;margin:8px auto 0;border:1.5px solid var(--ink);font-size:7px;font-weight:500;letter-spacing:1px;text-transform:uppercase;color:var(--ink);text-align:center;line-height:19px}

  .pair{display:flex;height:199px}
  .tile{position:relative;width:50%;height:100%}
  .tile--terrace{background:
      radial-gradient(ellipse 45% 18% at 40% 66%,rgba(240,170,90,.55),transparent 70%),
      linear-gradient(180deg,#27397a 0%,#34468a 35%,#3c4a6e 52%,#2a2a36 70%,#121a26 100%)}
  .tile--walkway{background:
      radial-gradient(ellipse 50% 40% at 80% 25%,rgba(150,170,210,.7),transparent 70%),
      linear-gradient(115deg,#2a1c16 0%,#6e4a30 35%,#a87a52 60%,#8a6446 80%,#4a3426 100%)}
  .tile--gazebo{background:
      radial-gradient(ellipse 55% 35% at 30% 25%,rgba(250,200,150,.7),transparent 70%),
      linear-gradient(180deg,#b47a5e 0%,#dca47c 32%,#8a6a70 55%,#4a3438 78%,#2a1e1e 100%)}
  .tile--suite{background:
      radial-gradient(ellipse 35% 40% at 78% 40%,rgba(235,230,215,.7),transparent 70%),
      linear-gradient(180deg,#7a5a38 0%,#b8986c 35%,#9a7a56 62%,#4a3424 100%)}
  .tile-caption{position:absolute;left:24px;bottom:22px;color:var(--paper)}
  .tile-title{font-family:var(--font-head);font-weight:400;font-size:10px;letter-spacing:.4px;text-transform:uppercase;line-height:11px}
  .tile-sub{font-size:8px;line-height:10px}

  .feature{height:142px;background:var(--mist);padding:20px 22px 0}
  .feature .copy{font-size:7.8px;letter-spacing:-.05px}
  .feature-title{font-family:var(--font-head);font-weight:400;font-size:13.5px;letter-spacing:.5px;text-align:center;text-transform:uppercase;color:var(--ink);margin-bottom:6px}

  .lounge{height:206px;background:
      radial-gradient(ellipse 18% 28% at 88% 48%,rgba(255,200,130,.75),transparent 70%),
      radial-gradient(ellipse 50% 22% at 50% 78%,rgba(230,200,170,.35),transparent 70%),
      linear-gradient(180deg,#1c3a82 0%,#26468a 30%,#3a4460 48%,#5a4632 62%,#6e5238 78%,#2a1f18 100%)}

  .footer{height:175px;background:var(--ink);color:var(--paper);padding-top:21px}
  .footer-note{font-size:8px;line-height:15px;text-align:center}
  .contacts{display:flex;justify-content:space-between;padding:0 12px 0 18px;margin-top:27px;text-align:center}
  .contact{width:110px}
  .contact-label{font-family:var(--font-head);font-weight:400;font-size:6.5px;letter-spacing:.8px;text-transform:uppercase;line-height:10px}
  .contact-value{font-size:8px;line-height:15px;margin-top:2px}
  .social{display:flex;justify-content:center;gap:7px;margin-top:20px}
  .social-item{width:15px;height:15px}
</style>
</head>
<body>
  <svg width="0" height="0" style="position:absolute" aria-hidden="true">
    <defs>
      <g id="social-mark">
        <rect x="2.6" y="2.6" width="9.8" height="9.8" fill="none" stroke="#fff" stroke-width=".9" transform="rotate(45 7.5 7.5)"/>
        <circle cx="7.5" cy="7.5" r="1.7" fill="#fff"/>
      </g>
    </defs>
  </svg>

  <div class="board-title">TEMPLATE 1</div>

  <!-- Full-length preview -->
  <div class="sheet sheet--full">
    <div class="email">
      <header class="masthead"><span class="brand">Corvan Meadow</span></header>
      <div class="hero photo" role="img" aria-label="Hotel pool terrace at dusk with palm trees and a city skyline">
        <h1 class="hero-title">Lorem ipsum<br>dolor sit amet<br>consectetur</h1>
      </div>
      <section class="intro">
        <p class="copy">Lorem ipsum dolor sit amet, consectetur adipiscing elit. Curabitur auctor sem in magna interdum rutrum. Quisque sit amet libero consequat. Curabitur auctor sem in magna interdum rutrum. Quisque sit amet libero consequat.</p>
        <span class="button">Contact us</span>
      </section>
      <section class="pair">
        <div class="tile tile--terrace photo" role="img" aria-label="Lakeside restaurant terrace lit at night"><div class="tile-caption"><div class="tile-title">Lorem ipsum</div><div class="tile-sub">Dolor sit amet</div></div></div>
        <div class="tile tile--walkway photo" role="img" aria-label="Hotel walkway with lanterns at dusk"><div class="tile-caption"><div class="tile-title">Lorem ipsum</div><div class="tile-sub">Dolor sit amet</div></div></div>
      </section>
      <section class="feature">
        <h2 class="feature-title">Lorem ipsum dolor sit amet</h2>
        <p class="copy">Lorem ipsum dolor sit amet, consectetur adipiscing elit. Curabitur auctor sem in magna interdum rutrum. Quisque sit amet libero consequat, facilisis neque non, egestas tortor. Ut egestas mollis ornare. Pellentesque ut ultricies tellus, id rutrum nisl. Fusce ullamcorper finibus dolor ac tristique. Aenean sit amet felis eget velit sollicitudin maximus eu et ligula. Nullam sed enim vel risus finibus semper nec ac ex.</p>
      </section>
      <section class="pair">
        <div class="tile tile--gazebo photo" role="img" aria-label="Beach gazebo at sunset overlooking the sea"><div class="tile-caption"><div class="tile-title">Lorem ipsum</div><div class="tile-sub">Dolor sit amet</div></div></div>
        <div class="tile tile--suite photo" role="img" aria-label="Warmly lit hotel suite with bed and sofa"><div class="tile-caption"><div class="tile-title">Lorem ipsum</div><div class="tile-sub">Dolor sit amet</div></div></div>
      </section>
      <section class="feature">
        <h2 class="feature-title">Lorem ipsum dolor sit amet</h2>
        <p class="copy">Lorem ipsum dolor sit amet, consectetur adipiscing elit. Curabitur auctor sem in magna interdum rutrum. Quisque sit amet libero consequat, facilisis neque non, egestas tortor. Ut egestas mollis ornare. Pellentesque ut ultricies tellus, id rutrum nisl. Fusce ullamcorper finibus dolor ac tristique. Aenean sit amet felis eget velit sollicitudin maximus eu et ligula. Nullam sed enim vel risus finibus semper nec ac ex.</p>
      </section>
      <div class="lounge photo" role="img" aria-label="Guests relaxing in an evening outdoor lounge under palm trees"></div>
      <footer class="footer">
        <p class="footer-note">Lorem ipsum dolor sit amet, consectetur adipiscing elit.<br>Curabitur auctor sem in magna interdum rutrum.</p>
        <div class="contacts">
          <div class="contact"><div class="contact-label">London address</div><div class="contact-value">41 Fenwick Lane,<br>London EC1V 9QT</div></div>
          <div class="contact"><div class="contact-label">Dubai address</div><div class="contact-value">Marlow Tower,<br>Saffra Rd, Dubai</div></div>
          <div class="contact"><div class="contact-label">Email</div><div class="contact-value">info@corvanmeadow.com</div></div>
        </div>
        <div class="social" aria-label="Social links">
          <svg class="social-item" viewBox="0 0 15 15"><use href="#social-mark"/></svg>
          <svg class="social-item" viewBox="0 0 15 15"><use href="#social-mark"/></svg>
          <svg class="social-item" viewBox="0 0 15 15"><use href="#social-mark"/></svg>
          <svg class="social-item" viewBox="0 0 15 15"><use href="#social-mark"/></svg>
          <svg class="social-item" viewBox="0 0 15 15"><use href="#social-mark"/></svg>
          <svg class="social-item" viewBox="0 0 15 15"><use href="#social-mark"/></svg>
        </div>
      </footer>
    </div>
  </div>

  <!-- Upper detail -->
  <div class="sheet sheet--upper">
    <div class="email">
      <header class="masthead"><span class="brand">Corvan Meadow</span></header>
      <div class="hero photo" role="img" aria-label="Hotel pool terrace at dusk with palm trees and a city skyline">
        <h1 class="hero-title">Lorem ipsum<br>dolor sit amet<br>consectetur</h1>
      </div>
      <section class="intro">
        <p class="copy">Lorem ipsum dolor sit amet, consectetur adipiscing elit. Curabitur auctor sem in magna interdum rutrum. Quisque sit amet libero consequat. Curabitur auctor sem in magna interdum rutrum. Quisque sit amet libero consequat.</p>
        <span class="button">Contact us</span>
      </section>
      <section class="pair">
        <div class="tile tile--terrace photo" role="img" aria-label="Lakeside restaurant terrace lit at night"><div class="tile-caption"><div class="tile-title">Lorem ipsum</div><div class="tile-sub">Dolor sit amet</div></div></div>
        <div class="tile tile--walkway photo" role="img" aria-label="Hotel walkway with lanterns at dusk"><div class="tile-caption"><div class="tile-title">Lorem ipsum</div><div class="tile-sub">Dolor sit amet</div></div></div>
      </section>
      <section class="feature">
        <h2 class="feature-title">Lorem ipsum dolor sit amet</h2>
        <p class="copy">Lorem ipsum dolor sit amet, consectetur adipiscing elit. Curabitur auctor sem in magna interdum rutrum. Quisque sit amet libero consequat, facilisis neque non, egestas tortor. Ut egestas mollis ornare. Pellentesque ut ultricies tellus, id rutrum nisl. Fusce ullamcorper finibus dolor ac tristique. Aenean sit amet felis eget velit sollicitudin maximus eu et ligula. Nullam sed enim vel risus finibus semper nec ac ex.</p>
      </section>
    </div>
  </div>

  <!-- Lower detail -->
  <div class="sheet sheet--lower">
    <div class="email">
      <section class="pair">
        <div class="tile tile--gazebo photo" role="img" aria-label="Beach gazebo at sunset overlooking the sea"><div class="tile-caption"><div class="tile-title">Lorem ipsum</div><div class="tile-sub">Dolor sit amet</div></div></div>
        <div class="tile tile--suite photo" role="img" aria-label="Warmly lit hotel suite with bed and sofa"><div class="tile-caption"><div class="tile-title">Lorem ipsum</div><div class="tile-sub">Dolor sit amet</div></div></div>
      </section>
      <section class="feature">
        <h2 class="feature-title">Lorem ipsum dolor sit amet</h2>
        <p class="copy">Lorem ipsum dolor sit amet, consectetur adipiscing elit. Curabitur auctor sem in magna interdum rutrum. Quisque sit amet libero consequat, facilisis neque non, egestas tortor. Ut egestas mollis ornare. Pellentesque ut ultricies tellus, id rutrum nisl. Fusce ullamcorper finibus dolor ac tristique. Aenean sit amet felis eget velit sollicitudin maximus eu et ligula. Nullam sed enim vel risus finibus semper nec ac ex.</p>
      </section>
      <div class="lounge photo" role="img" aria-label="Guests relaxing in an evening outdoor lounge under palm trees"></div>
      <footer class="footer">
        <p class="footer-note">Lorem ipsum dolor sit amet, consectetur adipiscing elit.<br>Curabitur auctor sem in magna interdum rutrum.</p>
        <div class="contacts">
          <div class="contact"><div class="contact-label">London address</div><div class="contact-value">41 Fenwick Lane,<br>London EC1V 9QT</div></div>
          <div class="contact"><div class="contact-label">Dubai address</div><div class="contact-value">Marlow Tower,<br>Saffra Rd, Dubai</div></div>
          <div class="contact"><div class="contact-label">Email</div><div class="contact-value">info@corvanmeadow.com</div></div>
        </div>
        <div class="social" aria-label="Social links">
          <svg class="social-item" viewBox="0 0 15 15"><use href="#social-mark"/></svg>
          <svg class="social-item" viewBox="0 0 15 15"><use href="#social-mark"/></svg>
          <svg class="social-item" viewBox="0 0 15 15"><use href="#social-mark"/></svg>
          <svg class="social-item" viewBox="0 0 15 15"><use href="#social-mark"/></svg>
          <svg class="social-item" viewBox="0 0 15 15"><use href="#social-mark"/></svg>
          <svg class="social-item" viewBox="0 0 15 15"><use href="#social-mark"/></svg>
        </div>
      </footer>
    </div>
  </div>
</body>
</html>
```